Billboard design for a small town Oral Surgeon

We are getting several billboards and need a design that highlights the doctors photo, and bullet points of what he does. Our business name is extremely long, so it’s a challenge to figure out how to do this. Maybe just use our logo? Open to ideas.
The logo can be shortened as designer sees fit, meaning we can drop the tag line. Important info to include:
Doctors name is Tobin Marek
The highlighted bullet points are:
•Implants
•wisdom teeth
•Jaw Surgery
•facial trauma
The goal of this billboard is to let our community know that they have an option here in Ada, our town. Many still drive to the city a couple hours away not knowing they now have an option here at home. Having a hard time finding examples of what I have in mind, so hoping this will get us going. I want it as “non-busy” as possible, so no unnecessary lines or anything that competes with the information we are trying to get across.

Target Market(s)

Everyone in town, just trying to spread the word that we are here

Industry/Entity Type

Medical/surgical (oral surgery)

Font styles to use
Sans Serif

Colors
0094D4
00A9DD
6FCCEA
C7EBF8
E9F6FB

Requirements
Must have
• *New note** Due to location of billboard, I prefer the photo of doctor to be on the left side. Must look neat and professional. Must highlight what we do.
Nice to have
• Our colors are a blue-green with silver, against black or white, but I’m flexible on this, I don’t necessarily need the colors highlighted. I’m also flexible on font style, just needs to be easy to read.
Should not have
• Distracting graphics, should not look like a dental office. That’s an issue we have is people thinking we are another dental office, we do not do any general dentistry, it’s surgery only.

```html
<!DOCTYPE html>
<html lang="en">
<head>
<meta charset="utf-8">
<title>Redbud Oral Surgery Billboard</title>
<link rel="stylesheet" href="https://fonts.googleapis.com/css2?family=Montserrat:wght@700;800&display=swap">
<style>
  :root {
    --page-bg: #c9c9c9;
    --board-dark: #0d0d0d;
    --board-mid: #3b3b3d;
    --teal: #1591ad;
    --silver: #9c9c9e;
    --white: #ffffff;
    --red: #e3202b;
    --photo-top: #6b5a4e;
    --photo-bottom: #1a2030;
  }
  html, body {
    margin: 0;
    width: 1200px;
    height: 1058px;
    overflow: hidden;
    background: var(--page-bg);
    font-family: "Montserrat", Arial, sans-serif;
  }
  .billboard {
    position: absolute;
    left: 20px;
    top: 335px;
    width: 1160px;
    height: 388px;
    background: radial-gradient(ellipse 60% 90% at 45% 40%, var(--board-mid) 0%, #1e1e1f 55%, var(--board-dark) 100%);
    overflow: hidden;
  }
  .doctor-photo {
    position: absolute;
    left: 0;
    top: 17px;
    width: 300px;
    height: 302px;
    background: linear-gradient(180deg, var(--photo-top) 0%, #3a3433 50%, var(--photo-bottom) 100%);
  }
  .doctor-name {
    position: absolute;
    left: 224px;
    top: 228px;
    margin: 0;
    color: var(--white);
    font-weight: 800;
    font-size: 29px;
    line-height: 27px;
    text-transform: uppercase;
  }
  .brand-name {
    position: absolute;
    left: 360px;
    top: 120px;
    width: 250px;
    margin: 0;
    color: var(--silver);
    font-weight: 800;
    font-size: 34px;
    line-height: 40px;
    text-align: center;
    text-transform: uppercase;
  }
  .services {
    position: absolute;
    left: 660px;
    top: 34px;
    margin: 0;
    padding: 0;
    list-style: none;
  }
  .services li {
    display: flex;
    align-items: center;
    height: 62px;
    color: var(--white);
    font-weight: 800;
    font-size: 47px;
    letter-spacing: 0.5px;
    text-transform: uppercase;
  }
  .services svg { width: 48px; height: 48px; margin-right: 22px; flex: none; }
  .location-tag {
    position: absolute;
    right: 0;
    top: 284px;
    width: 216px;
    height: 35px;
    background: var(--red);
    clip-path: polygon(8px 0, 100% 0, 100% 100%, 0 100%);
    display: flex;
    align-items: center;
    justify-content: center;
    gap: 6px;
    color: var(--white);
    font-weight: 800;
    font-size: 19px;
    text-transform: uppercase;
  }
  .location-tag svg { width: 16px; height: 22px; }
  .contact-bar {
    position: absolute;
    left: 0;
    bottom: 0;
    width: 100%;
    height: 69px;
    background: var(--board-dark);
    display: flex;
    align-items: center;
    justify-content: center;
    color: var(--white);
    font-weight: 800;
    font-size: 43px;
    letter-spacing: -0.3px;
  }
  .contact-bar .divider {
    display: inline-block;
    width: 2px;
    height: 44px;
    background: var(--white);
    margin: 0 14px;
  }
</style>
</head>
<body>
  <div class="billboard">
    <div class="doctor-photo" role="img" aria-label="Portrait photo of Dr. Tobin Marek in a dark suit and red tie"></div>
    <p class="doctor-name">Tobin<br>Marek</p>

    <p class="brand-name">Redbud<br>Oral<br>Surgery</p>

    <ul class="services">
      <li><svg viewBox="0 0 48 48" aria-hidden="true"><circle cx="24" cy="24" r="24" fill="var(--teal)"/><path d="M13 25 L21 33 L36 16" fill="none" stroke="#fff" stroke-width="6" stroke-linecap="round" stroke-linejoin="round"/></svg>Implants</li>
      <li><svg viewBox="0 0 48 48" aria-hidden="true"><circle cx="24" cy="24" r="24" fill="var(--teal)"/><path d="M13 25 L21 33 L36 16" fill="none" stroke="#fff" stroke-width="6" stroke-linecap="round" stroke-linejoin="round"/></svg>Wisdom Teeth</li>
      <li><svg viewBox="0 0 48 48" aria-hidden="true"><circle cx="24" cy="24" r="24" fill="var(--teal)"/><path d="M13 25 L21 33 L36 16" fill="none" stroke="#fff" stroke-width="6" stroke-linecap="round" stroke-linejoin="round"/></svg>Jaw Surgery</li>
      <li><svg viewBox="0 0 48 48" aria-hidden="true"><circle cx="24" cy="24" r="24" fill="var(--teal)"/><path d="M13 25 L21 33 L36 16" fill="none" stroke="#fff" stroke-width="6" stroke-linecap="round" stroke-linejoin="round"/></svg>Facial Trauma</li>
    </ul>

    <div class="location-tag">
      <svg viewBox="0 0 16 22" aria-hidden="true"><path d="M8 1 C4 1 1 4 1 8 C1 13 8 21 8 21 C8 21 15 13 15 8 C15 4 12 1 8 1 Z" fill="#fff"/><circle cx="8" cy="8" r="3" fill="var(--red)"/></svg>
      We are in Ada
    </div>

    <div class="contact-bar">
      <span class="phone">(580) 555-0142</span>
      <span class="divider"></span>
      <span class="website">www.redbudoralsurgery.com</span>
    </div>
  </div>
</body>
</html>
```